KLT Website Homepage Redesign

My website needs a homepage redesign and banner photos updates for Discovery and SEO Services pages. We sell Search Engine Optimization services. We use Search Engine Optimization techniques to help our clients rank high in search engines like Zorvix. It is an intense competition to consistently rank above other businesses. The problem is there is no easy way to show what the benefits of Search Engine Optimization services look like in an emotional way. I want to use an image from sailboat racing to dramatize that our clients win at Search Engine Optimization marketing.
The following products are desired:
1. Desktop version homepage redesign with a banner that clearly shows we sell Search Engine Optimization services using sailboat racing as a metaphor.
2. Mobile version homepage redesign with a banner that clearly shows we sell Search Engine Optimization services using sailboat racing as a metaphor.
2. New banner photo for the Discovery Page
3. New banner photo for the SEO page
The design must be responsive and show well on desktops, laptops, tablets and mobile phones. The current footer style must be kept. A third service called SEO must be added.
the website URL is www.velmorbix.com
Target Market(s)
Business to Business
Industry/Entity Type
Digital Marketing
Coding
Coded - Design and coding required
Number of Pages Required
1 page
Colors
Designer to choose colors to be used in the design.
Look and feel
Each slider illustrates characteristics of the customer's brand and the style your logo design should communicate.

```html
<!DOCTYPE html>
<html lang="en">
<head>
<meta charset="utf-8">
<title>KLT Digital — Homepage</title>
<link href="https://fonts.googleapis.com/css2?family=Montserrat:wght@400;500;600&family=Varela+Round&display=swap" rel="stylesheet">
<style>
:root{
  --blue:#3d73be;
  --blue-dark:#2f5f9f;
  --yellow:#f7c92b;
  --ink:#1f2430;
  --muted:#555b66;
  --band:#eef5fb;
  --line:#d9dfe7;
  --white:#ffffff;
  --field:#f2f4f8;
}
*{margin:0;padding:0;box-sizing:border-box}
html,body{width:1200px;height:3673px;overflow:hidden;background:var(--white)}
body{position:relative;font-family:"Montserrat",sans-serif;color:var(--ink)}
.abs{position:absolute}
.heading{font-family:"Varela Round",sans-serif;font-weight:400;color:var(--ink)}
.center{left:0;width:1200px;text-align:center}
.btn{position:absolute;border-radius:20px;font-size:12px;font-weight:500;display:flex;align-items:center;justify-content:center;z-index:3}
.btn-blue{background:var(--blue);color:var(--white)}
.btn-yellow{background:var(--yellow);color:var(--ink)}
svg.wave{position:absolute;left:0;width:1200px;display:block}

.nav{top:0;left:0;width:1200px;height:80px;background:var(--white)}
.logo{font-family:"Varela Round",sans-serif;color:var(--blue);font-size:26px;line-height:1}
.logo small{display:block;font-size:17px;margin-top:2px}
.nav-links{left:320px;top:32px;display:flex;gap:40px;font-size:12px;color:var(--ink)}
.nav-links .active{color:var(--blue)}
.nav-phone{left:806px;top:31px;font-size:14px;color:var(--blue);display:flex;gap:6px;align-items:center}

.hero-photo{top:80px;left:0;width:1200px;height:620px;background:linear-gradient(100deg,#3a4a63 0%,#6c7890 40%,#9aa3b3 65%,#6f6a63 100%)}
.hero-kicker{left:88px;top:192px;font-size:18px;color:var(--yellow)}
.hero-title{left:88px;top:240px;font-size:23px;line-height:29px;color:var(--white);font-family:"Varela Round",sans-serif;font-weight:400}

.mission-title{top:666px;font-size:29px;line-height:35px}
.mission-text{top:768px;left:210px;width:780px;font-size:12px;line-height:19px;color:var(--muted);text-align:center}
.mission-text p+p{margin-top:19px}

.band{left:0;width:1200px;background:var(--band)}

.section-title{font-size:28px}
.service{width:240px;text-align:center;font-size:19px;font-family:"Varela Round",sans-serif;line-height:23px}
.service-box{left:792px;top:1175px;width:320px;height:215px;border:1px solid var(--blue);background:var(--white)}
.sub{width:210px;text-align:center}
.sub h3{font-family:"Montserrat",sans-serif;font-weight:500;font-size:15px;margin-bottom:10px}
.sub p{font-size:11.5px;line-height:17.5px;color:var(--muted)}
.sub .more{display:block;margin-top:16px;font-size:11.5px;font-weight:600;color:var(--blue)}
.ring{width:96px;height:96px;border-radius:50%;border:5px solid #d6e4f3;background:var(--white)}

.aud{width:220px;text-align:center;font-size:15px;font-weight:500;line-height:20px}

.client-badge{width:120px;height:120px;border-radius:50%;background:var(--white);display:flex;align-items:center;justify-content:center;font-size:13px;font-weight:600;color:#2e7d4f}
.client-badge::before{content:"";position:absolute;left:-6px;top:-6px;width:80px;height:132px;border-radius:60px 0 0 60px;background:var(--yellow);z-index:-1}
.quote{width:300px;font-size:11.5px;line-height:21px;color:var(--muted)}
.quote-name{font-size:14px;font-weight:500;color:var(--ink)}
.quote-link{font-size:12px;font-weight:600;color:var(--blue)}

.field{position:absolute;z-index:3;height:32px;border-radius:16px;background:var(--field);font-size:11px;color:#6b7280;padding-left:20px;display:flex;align-items:center}

.footer-photo{left:0;top:3240px;width:1200px;height:433px;background:linear-gradient(180deg,#f3f6fa 0%,#e7edf4 60%,#dfe6ee 100%)}
.foot-title{font-size:17px;font-family:"Varela Round",sans-serif}
.foot-list{font-size:12px;line-height:24px;color:var(--ink);list-style:none}
.social{width:30px;height:30px;border-radius:50%;background:#1e3a6b}
.social.on{background:var(--yellow)}
</style>
</head>
<body>

<div class="abs hero-photo" role="img" aria-label="Laptop screen showing an SEO mind map of content, backlinks, headings and social media on a desk"></div>

<header class="abs nav">
  <div class="abs logo" style="left:88px;top:14px">KLT<small>Digital</small></div>
  <nav class="abs nav-links">
    <span class="active">Home</span><span>About Us</span><span>Services</span><span>Testimonials</span><span>Let's Talk</span>
  </nav>
  <div class="abs nav-phone">
    <svg width="16" height="16" viewBox="0 0 24 24" fill="none" stroke="currentColor" stroke-width="2"><path d="M5 3h4l2 5-3 2a12 12 0 0 0 6 6l2-3 5 2v4a2 2 0 0 1-2 2A18 18 0 0 1 3 5a2 2 0 0 1 2-2z"/></svg>
    +123 555 0190
  </div>
  <div class="btn btn-blue" style="left:984px;top:24px;width:128px;height:32px">Contact Us</div>
</header>

<div class="abs hero-kicker">Are you ready to take the lead?</div>
<h1 class="abs hero-title">It’s KLT Digital’s mission<br>to empower every client with the web<br>presence that will drive them ahead<br>of the competition.</h1>
<div class="btn btn-yellow" style="left:88px;top:390px;width:128px;height:32px">Contact Now!</div>

<svg class="wave" style="top:540px" height="170" viewBox="0 0 1200 170" preserveAspectRatio="none">
  <path d="M0 45 C300 0 560 -10 780 20 C960 45 1100 90 1200 120 V170 H0 Z" fill="#ffffff"/>
  <path d="M740 15 C940 40 1100 95 1200 118 V162 C1100 120 960 70 740 15 Z" fill="#3d73be"/>
</svg>

<h2 class="abs heading center mission-title">Our mission is to empower every client with the<br>web presence that will drive them</h2>
<div class="abs mission-text">
  <p>We enable businesses to take the lead online with websites built on a smart foundation and with the robust features and digital strategy that give every client the competitive edge needed in today’s world.</p>
  <p>Our team of industry experts allows you to have a one-stop-shop for business discovery, website strategy, advanced SEO, design and development, content creation, marketing, hosting, and technical support. Whether your project requires a digital marketer, web strategist, copywriter or editor, multi-media producer ...</p>
</div>

<div class="abs band" style="top:900px;height:1080px"></div>
<svg class="wave" style="top:880px" height="170" viewBox="0 0 1200 170" preserveAspectRatio="none">
  <path d="M0 0 H1200 V62 C1000 140 720 160 560 150 C360 136 150 80 0 20 Z" fill="#ffffff"/>
  <path d="M0 20 C150 80 360 136 560 150 C380 150 160 110 0 62 Z" fill="#3d73be"/>
</svg>
<div class="btn btn-blue" style="left:536px;top:918px;width:128px;height:30px">About Us</div>

<h2 class="abs heading center section-title" style="top:1108px">Services We Provide</h2>

<div class="abs service-box"></div>
<svg class="abs" style="left:945px;top:1389px" width="14" height="8" viewBox="0 0 14 8"><path d="M0 0 L7 7 L14 0 Z" fill="#3d73be"/></svg>

<svg class="abs" style="left:198px;top:1205px" width="100" height="100" viewBox="0 0 100 100" fill="none" stroke-width="4">
  <circle cx="42" cy="42" r="34" stroke="#3d73be"/><circle cx="42" cy="42" r="27" stroke="#f7c92b"/>
  <path d="M66 66 L92 92" stroke="#3d73be" stroke-width="8" stroke-linecap="round"/>
  <path d="M24 50 L36 34 L48 46 L62 28" stroke="#f7c92b"/>
</svg>
<div class="abs service" style="left:128px;top:1322px">SEO Audit</div>

<svg class="abs" style="left:550px;top:1205px" width="100" height="100" viewBox="0 0 100 100" fill="none" stroke="#3d73be" stroke-width="3.5">
  <rect x="32" y="4" width="36" height="24" rx="4" stroke="#f7c92b"/>
  <circle cx="14" cy="30" r="7"/><circle cx="86" cy="30" r="7"/>
  <path d="M4 70 V46 a10 10 0 0 1 20 0 V60 H40 M96 70 V46 a10 10 0 0 0-20 0 V60 H60"/>
  <path d="M20 62 H80 M36 62 V96 M50 62 V96 M64 62 V96"/>
</svg>
<div class="abs service" style="left:480px;top:1322px">SEO Consulting</div>

<svg class="abs" style="left:902px;top:1206px" width="100" height="90" viewBox="0 0 100 90" fill="none" stroke="#3d73be" stroke-width="3.5">
  <rect x="2" y="4" width="80" height="78" rx="3"/><path d="M2 16 H82"/>
  <path d="M26 42 L16 50 L26 58 M44 42 L52 58 M60 42 L70 50 L60 58" stroke="#f7c92b"/>
  <path d="M70 88 L76 64 L92 58 L98 74 L84 84 Z" stroke="#f7c92b"/>
</svg>
<div class="abs service" style="left:832px;top:1316px">Website Design,<br>Development &amp; Hosting.</div>

<div class="abs ring" style="left:156px;top:1455px"></div>
<svg class="abs" style="left:180px;top:1480px" width="48" height="46" viewBox="0 0 48 46" fill="none" stroke="#3d73be" stroke-width="2.5"><rect x="2" y="2" width="44" height="32" rx="2"/><path d="M16 44 H32 M24 34 V44 M10 12 H26 M10 20 H24 M10 27 H22 M30 26 L40 10"/></svg>
<div class="abs sub" style="left:99px;top:1572px"><h3>Website Strategy</h3><p>A strong company website increases leads and reduces bounces by giving a visitor exactly exactly ...</p><span class="more">Read More →</span></div>

<div class="abs ring" style="left:420px;top:1455px"></div>
<svg class="abs" style="left:444px;top:1480px" width="48" height="46" viewBox="0 0 48 46" fill="none" stroke="#3d73be" stroke-width="2.5"><rect x="2" y="2" width="44" height="40" rx="2"/><path d="M2 12 H46 M10 22 H24 M10 30 H20 M26 36 L40 18 L44 22 L30 40 Z"/></svg>
<div class="abs sub" style="left:363px;top:1572px"><h3>Web Writing Services</h3><p>Well-crafted web writing is a balancing act between message, brand voice, audience expecta-tion, and SEO ...</p><span class="more">Read More →</span></div>

<div class="abs ring" style="left:684px;top:1455px"></div>
<svg class="abs" style="left:708px;top:1480px" width="48" height="46" viewBox="0 0 48 46" fill="none" stroke="#3d73be" stroke-width="2.5"><rect x="2" y="2" width="40" height="36" rx="2"/><path d="M2 12 H42"/><circle cx="28" cy="28" r="8"/><circle cx="28" cy="28" r="3"/></svg>
<div class="abs sub" style="left:627px;top:1572px"><h3>Advanced Web Tools</h3><p>CRM or API integration, ecom-merce capabilities, advanced calendars and forms—whatever you might need ...</p><span class="more">Read More →</span></div>

<div class="abs ring" style="left:948px;top:1455px"></div>
<svg class="abs" style="left:972px;top:1480px" width="48" height="46" viewBox="0 0 48 46" fill="none" stroke="#3d73be" stroke-width="2.5"><rect x="2" y="2" width="30" height="12" rx="2"/><rect x="2" y="18" width="30" height="12" rx="2"/><rect x="2" y="34" width="30" height="10" rx="2"/><circle cx="38" cy="24" r="7"/><path d="M34 10 H46 M36 40 H46"/></svg>
<div class="abs sub" style="left:891px;top:1572px"><h3>Hosting &amp; Support</h3><p>A reliable hosting environment is the difference between a web-site that is fast or slow, vulnerable ...</p><span class="more">Read More →</span></div>

<div class="btn btn-yellow" style="left:500px;top:1767px;width:200px;height:32px">Contact KLT Digital</div>

<svg class="wave" style="top:1860px" height="180" viewBox="0 0 1200 180" preserveAspectRatio="none">
  <path d="M0 40 C300 5 560 -5 800 25 C1000 50 1140 100 1200 130 V180 H0 Z" fill="#ffffff"/>
  <path d="M560 22 C860 30 1080 80 1200 112 V170 C1080 110 880 50 560 22 Z" fill="#3d73be"/>
</svg>

<h2 class="abs heading center section-title" style="top:1982px">Who Do We Work With?</h2>
<p class="abs center" style="top:2036px;font-size:12px;line-height:19px;color:var(--muted)">There are many variations of passages of Lorem Ipsum available, but the majority have suffered alteration<br>some form, by injected humour, or randomised words which don't look</p>

<div class="abs band" style="top:2226px;height:630px"></div>
<svg class="wave" style="top:2160px" height="180" viewBox="0 0 1200 180" preserveAspectRatio="none">
  <path d="M0 0 H1200 V80 C1000 150 720 172 570 168 C360 160 150 100 0 35 Z" fill="#ffffff"/>
  <path d="M0 35 C150 100 360 160 570 168 C380 170 160 130 0 80 Z" fill="#3d73be"/>
</svg>

<svg class="abs" style="left:186px;top:2112px" width="36" height="34" viewBox="0 0 36 34" fill="none" stroke="#3d73be" stroke-width="2.5"><path d="M2 2 V32 H34 M6 24 L14 14 L22 20 L32 6"/></svg>
<div class="abs aud" style="left:94px;top:2159px">Startups</div>
<svg class="abs" style="left:448px;top:2110px" width="40" height="36" viewBox="0 0 40 36" fill="none" stroke="#3d73be" stroke-width="2.5"><rect x="2" y="8" width="36" height="26" rx="2"/><path d="M14 8 V3 H26 V8 M2 18 H38"/></svg>
<div class="abs aud" style="left:358px;top:2159px">Small to Medium-Sized<br>Businesses</div>
<svg class="abs" style="left:712px;top:2108px" width="40" height="38" viewBox="0 0 40 38" fill="none" stroke="#3d73be" stroke-width="2.5"><path d="M20 16 C10 8 14 2 20 6 C26 2 30 8 20 16 Z M2 26 L14 20 H26 L18 26 L30 22 L38 24 L22 34 L10 32 Z"/></svg>
<div class="abs aud" style="left:622px;top:2159px">Nonprofits<br>Government Agencies</div>
<svg class="abs" style="left:976px;top:2110px" width="40" height="36" viewBox="0 0 40 36" fill="none" stroke="#3d73be" stroke-width="2.5"><path d="M2 4 H8 L13 24 H33 L37 10 H10"/><circle cx="15" cy="31" r="3"/><circle cx="31" cy="31" r="3"/></svg>
<div class="abs aud" style="left:886px;top:2159px">ECommerce<br>Marketplaces</div>

<h2 class="abs heading center section-title" style="top:2404px">What Our Clients Say</h2>

<svg class="abs" style="left:72px;top:2532px" width="18" height="16" viewBox="0 0 18 16" fill="none" stroke="#9aa3b3" stroke-width="2"><path d="M17 8 H2 M8 2 L2 8 L8 14"/></svg>
<svg class="abs" style="left:1112px;top:2532px" width="18" height="16" viewBox="0 0 18 16" fill="none" stroke="#9aa3b3" stroke-width="2"><path d="M1 8 H16 M10 2 L16 8 L10 14"/></svg>

<div class="abs" style="left:140px;top:2474px;z-index:1"><div class="client-badge" style="position:relative">Brightlane</div></div>
<p class="abs quote" style="left:284px;top:2480px">Daniel Ashcombe is an author, noted Leadership curriculum designer and trainer to Fortune 500 companies. After completing his book, he decided to focus his career on curric-ulum development for customers that require train-the-trainer services and leadership coaching ...</p>
<div class="abs quote-name" style="left:284px;top:2650px">Northfield Learning Institute</div>
<div class="abs quote-link" style="left:284px;top:2675px">Visit Site →</div>

<div class="abs" style="left:640px;top:2474px;z-index:1"><div class="client-badge" style="position:relative">Brightlane</div></div>
<p class="abs quote" style="left:784px;top:2480px">As a surgeon in private practice, I seek to maintain a competitive edge in the areas of medical and business management technolo-gies. Therefore, I was an early adopter of electronic medical records.<br>I selected Marlow and his team to analyze my workflow processes to determine ...</p>
<div class="abs quote-name" style="left:784px;top:2648px">Clearwater Family Practice</div>
<div class="abs quote-link" style="left:784px;top:2673px">Visit Site →</div>

<div class="btn btn-blue" style="left:536px;top:2727px;width:128px;height:32px">View All</div>

<svg class="wave" style="top:2836px" height="180" viewBox="0 0 1200 180" preserveAspectRatio="none">
  <path d="M0 40 C300 5 560 -5 800 25 C1000 50 1140 100 1200 130 V180 H0 Z" fill="#ffffff"/>
  <path d="M560 22 C860 30 1080 80 1200 112 V170 C1080 110 880 50 560 22 Z" fill="#3d73be"/>
</svg>

<div class="abs footer-photo" role="img" aria-label="Faded photograph of racing sailboats on open water"></div>
<svg class="wave" style="top:3110px" height="190" viewBox="0 0 1200 190" preserveAspectRatio="none">
  <path d="M0 0 H1200 V70 C1000 150 720 180 570 176 C360 168 150 100 0 30 Z" fill="#ffffff"/>
  <path d="M0 30 C150 100 360 168 570 176 C380 178 160 130 0 78 Z" fill="#3d73be"/>
</svg>

<h2 class="abs heading center section-title" style="top:2938px">Are you Ready to Take the Lead?</h2>
<p class="abs center" style="top:2979px;font-size:12px;color:var(--muted)">Contact KLT Digital Today!</p>

<div class="field" style="left:312px;top:3029px;width:280px">Name</div>
<div class="field" style="left:608px;top:3029px;width:280px">Phone</div>
<div class="field" style="left:312px;top:3078px;width:280px">Email Address</div>
<div class="field" style="left:608px;top:3078px;width:280px">Company Name</div>
<div class="field" style="left:312px;top:3125px;width:568px">Select Your Service
  <svg style="position:absolute;right:14px;top:13px" width="10" height="6" viewBox="0 0 10 6" fill="none" stroke="#6b7280" stroke-width="1.4"><path d="M1 1 L5 5 L9 1"/></svg>
</div>
<div class="btn btn-yellow" style="left:544px;top:3173px;width:112px;height:32px">Submit</div>

<div class="abs logo" style="left:88px;top:3376px;font-size:40px">KLT<small style="font-size:26px">Digital</small></div>

<div class="abs foot-title" style="left:352px;top:3366px">Contact Us</div>
<div class="abs" style="left:352px;top:3414px;font-size:15px">Call Us: +123 555 0190</div>
<div class="abs" style="left:352px;top:3440px;font-size:12px">e. info@velmorbix.com</div>
<div class="abs" style="left:352px;top:3484px;font-size:12px;line-height:22px">450 Harbor Crest Way<br>Suite 210 Larkspur,<br>MD 21099</div>

<div class="abs foot-title" style="left:640px;top:3366px">Quick Links</div>
<ul class="abs foot-list" style="left:640px;top:3410px"><li>Home</li><li>Web Strategy</li><li>Support</li><li>SEO</li><li>Testimonials</li><li>Contact Us</li></ul>
<ul class="abs foot-list" style="left:785px;top:3410px"><li>Advanced Website Tools</li><li>Privacy</li><li>Terms of Use</li></ul>

<div class="abs social" style="left:1081px;top:3371px" aria-label="Social profile link"></div>
<div class="abs social on" style="left:1081px;top:3411px" aria-label="Social profile link"></div>
<div class="abs social" style="left:1081px;top:3451px" aria-label="Social profile link"></div>
<div class="abs social" style="left:1081px;top:3491px" aria-label="Social profile link"></div>

<div class="abs" style="left:88px;top:3600px;width:1024px;height:1px;background:var(--line)"></div>
<p class="abs center" style="top:3626px;font-size:11.5px;color:var(--muted)">© 2020 <span style="color:var(--blue)">KLT Digital.</span>&nbsp;&nbsp;&nbsp;&nbsp;All Rights Reserved.&nbsp;&nbsp;&nbsp;&nbsp;Web Strategy by KLT Digital</p>

</body>
</html>
```